Election campaign for community-managed mental health sector - Webpage Banner and Logo

Please refer to the attached design brief for all the information and details. This is a campaign logo, and graphic design for the webpage banner.

Target Market(s)

Primary • NSW Ministers, Shadow Ministers, MPs and political advisers • Treasury and health policy decision-makers • Other key decision makers and stakeholders Secondary • Community-managed mental health workers • Sector leaders and advocates • People with lived experience and their families

Industry/Entity Type

Community-managed mental health sector in NSW, Australia

Other font styles liked:
• Gotham Family

Requirements
Must have
• Please refer to design brief
Nice to have
Should not have
• Completely AI generated - see design brief for more information.

```html
<!DOCTYPE html>
<html lang="en">
<head>
<meta charset="utf-8">
<title>Campaign Banner</title>
<link rel="stylesheet" href="https://fonts.googleapis.com/css2?family=Montserrat:wght@400;500;700;800&display=swap">
<style>
  :root {
    --purple: #4b2385;
    --orange: #f5a623;
    --bg-start: #f2f7e4;
    --bg-end: #fdf0e2;
    --frame: #e4e0d8;
    --photo-a: #d9d4cc;
    --photo-b: #c98a3a;
  }
  * { margin: 0; padding: 0; box-sizing: border-box; }
  html, body { width: 1200px; height: 481px; overflow: hidden; }
  .banner {
    position: relative;
    width: 1200px;
    height: 481px;
    background: linear-gradient(115deg, var(--bg-start) 0%, #fbf4e4 45%, var(--bg-end) 100%);
    font-family: "Montserrat", sans-serif;
    color: var(--purple);
    overflow: hidden;
  }
  .brand {
    position: absolute;
    left: 67px;
    top: 69px;
    width: 120px;
    text-align: center;
  }
  .brand-mark {
    display: block;
    width: 36px;
    height: 38px;
    margin: 0 auto 16px;
    border-radius: 9px;
    background: var(--orange);
  }
  .brand-name {
    font-size: 11.5px;
    font-weight: 500;
    line-height: 14px;
    letter-spacing: 0.1px;
    color: var(--purple);
    white-space: nowrap;
  }
  .message {
    position: absolute;
    left: 82px;
    top: 188px;
    height: 97px;
    padding-left: 33px;
    border-left: 3px solid var(--purple);
  }
  .headline {
    font-size: 41px;
    font-weight: 800;
    line-height: 1;
    letter-spacing: 0.3px;
    margin-top: -3px;
    white-space: nowrap;
  }
  .subline {
    margin-top: 16px;
    font-size: 21.5px;
    font-weight: 500;
    line-height: 27px;
    letter-spacing: 0.4px;
    white-space: nowrap;
  }
  .photo-frame {
    position: absolute;
    left: 705px;
    top: 66px;
    width: 500px;
    height: 348px;
    border-radius: 8px 0 0 8px;
    background: var(--frame);
  }
  .photo {
    position: absolute;
    left: 716px;
    top: 78px;
    width: 484px;
    height: 324px;
    background: linear-gradient(135deg, var(--photo-a) 0%, #cfc5b6 50%, var(--photo-b) 100%);
  }
</style>
</head>
<body>
  <div class="banner">
    <div class="brand">
      <span class="brand-mark"></span>
      <p class="brand-name">CARE ALONGSIDE<br>NSW</p>
    </div>

    <div class="message">
      <h1 class="headline">Care alongside you.</h1>
      <p class="subline">Put community-based mental health<br>care first.</p>
    </div>

    <div class="photo-frame"></div>
    <div class="photo" role="img" aria-label="Photo of a support group seated in a circle on orange chairs, a facilitator holding a clipboard"></div>
  </div>
</body>
</html>
```